Mara Penwick Concert Poster

I am a fulltime Christian singer from NZ. I need a new Concert Poster.
Specs: Color pic supplied but prefer b&w. Portrait orientation, not landscape. Copy supplied (to appear on bottom half of poster). Need blank box or strip near bottom for local venue details. Signature-style 'Mara Penwick' title across the photo or across the top, but totally open to design ideas/suggestion.

Target Market(s)

Mainly churches where I sing..

Industry/Entity Type

Singer

Requirements
Must have
• From past experience I have found a dark (even black) background, has most impact, with copy reversed out.. But as above, I am open to suggestions re color and feel. View my music on Vidorra for additional feel ideas.
Nice to have
• Simple direct classy style best, with minimal clutter.

```html
<!DOCTYPE html>
<html lang="en">
<head>
<meta charset="utf-8">
<title>Mara Penwick Concert Poster</title>
<link rel="stylesheet" href="https://fonts.googleapis.com/css2?family=Oswald:wght@600;700&family=Roboto+Condensed:ital,wght@0,400;0,700;1,400&family=Open+Sans:wght@400;600&display=swap">
<style>
  :root {
    --bg: #1b1b1c;
    --band: #2b2b2d;
    --red: #d8232a;
    --white: #ffffff;
    --grey: #a9a9a9;
    --yellow: #f3d21c;
    --blue: #1f5fa8;
  }
  * { margin: 0; padding: 0; box-sizing: border-box; }
  html, body { width: 849px; height: 1200px; overflow: hidden; background: var(--bg); }
  .poster {
    position: relative;
    width: 849px;
    height: 1200px;
    background: var(--bg);
    font-family: "Roboto Condensed", Arial, sans-serif;
    color: var(--white);
    overflow: hidden;
  }
  .hero-photo {
    position: absolute;
    left: 0; top: 0;
    width: 849px; height: 598px;
    background:
      radial-gradient(ellipse at 68% 35%, #b9b2ad 0%, #8a8fa0 22%, rgba(120,40,40,0) 48%),
      linear-gradient(90deg, #5a1412 0%, #8e2320 30%, #7a1d1b 60%, #5c1614 100%);
  }
  .accent-strip {
    position: absolute;
    left: 430px; top: 600px;
    width: 419px; height: 18px;
    background: var(--red);
  }
  .artist-name {
    position: absolute;
    left: 68px; top: 606px;
    width: 360px;
    font-family: "Oswald", Impact, sans-serif;
    font-weight: 700;
    font-size: 98px;
    line-height: 112px;
    color: var(--red);
    text-transform: uppercase;
    letter-spacing: 0;
  }
  .credentials {
    position: absolute;
    left: 439px; top: 630px;
    width: 400px;
  }
  .credentials .intro {
    font-size: 20px; color: var(--grey); line-height: 26px;
  }
  .credentials .headline {
    font-weight: 700; font-size: 28px; line-height: 36px; margin-top: 4px;
  }
  .credentials .stats {
    font-size: 20px; line-height: 24px; color: var(--grey); margin-top: 4px;
  }
  .quote-band {
    position: absolute;
    left: 0; top: 852px;
    width: 849px; height: 126px;
    background: var(--band);
  }
  .quote-band .marker { position: absolute; top: 40px; }
  .quote-band .marker.left { left: 0; }
  .quote-band .marker.right { right: 0; }
  .quote-text {
    position: absolute;
    left: 70px; top: 16px;
    width: 720px;
    font-family: "Roboto Condensed", Arial, sans-serif;
    font-size: 36px;
    line-height: 46px;
    color: var(--yellow);
  }
  .quote-source {
    position: absolute;
    left: 556px; top: 80px;
    font-size: 17px; color: var(--white);
  }
  .info {
    position: absolute;
    top: 1036px;
    font-family: "Open Sans", Arial, sans-serif;
  }
  .info .label { font-size: 18px; color: var(--grey); line-height: 24px; }
  .info .value { font-size: 33px; color: var(--white); line-height: 44px; }
  .info.tour { left: 68px; }
  .info.venue { right: 54px; text-align: right; }
</style>
</head>
<body>
<main class="poster">
  <div class="hero-photo" role="img" aria-label="Photo of the singer holding an acoustic guitar in front of a red wooden wall"></div>
  <div class="accent-strip"></div>

  <h1 class="artist-name">Mara<br>Penwick</h1>

  <section class="credentials">
    <p class="intro">New Zealand's most</p>
    <p class="headline">Prolific &amp; Accomplished<br>Christian Singer/<br>Songwriter:</p>
    <p class="stats">12 albums, 3 Gold Albums,<br>2 Aotea Music Awards</p>
  </section>

  <section class="quote-band">
    <svg class="marker left" width="22" height="46" viewBox="0 0 22 46"><polygon points="0,0 22,23 0,46" fill="var(--blue)"/></svg>
    <svg class="marker right" width="22" height="46" viewBox="0 0 22 46"><polygon points="22,0 0,23 22,46" fill="var(--blue)"/></svg>
    <p class="quote-text">'There is a depth in your songs that is<br>very rare in Christian music today'</p>
    <p class="quote-source">Vidorra comment Aug 18, 2011</p>
  </section>

  <section class="info tour">
    <p class="label">Tour Schedule &amp; Info:</p>
    <p class="value">www.marapenwickmusic.com</p>
  </section>
  <section class="info venue">
    <p class="label">Venue:</p>
    <p class="value">VENUE</p>
  </section>
</main>
</body>
</html>
```